GUARANTEED! Simple website for independent event planner and consultant...

I need a website that is no more than 5 or 6 pages to illustrate who I am and what I can offer to groups who book hotels for meetings and conferences. I have 20 years of experience planning meetings within hotels and I am now ready to go out on my own and help clients choose venues, negotiate contracts and plan effective meetings. I will focus on clients planning meetings in the mountains of Colorado but I am willing to travel as well. I want to work with a person who is collaborative and can direct me on what they need to move the project along quickly. I already have my logo, a hosting site and work e-mail address. Also, I recently hired a photographer to do head shots. Lastly, it important for me to be able to talk on the phone or skype with this person, as needed and I must be able to make changes to my site down the road when necessary...

Target Market(s)

Corporate Groups

Industry/Entity Type

Event Planning

Coding

Coded - Design and coding required

Number of Pages Required

5+ page

Font styles to use
Sans Serif

Requirements
Must have
• About me page, event planning services offered page, task force and consulting work page, testimonials page, page for blogs, page to contact me/request a proposal. May need advice on what else I need...
Nice to have
• I want it to look sharp and professional. I want people to look at my site and know immediately that they can trust me and the work I can do.
• I don't want it to look like it is over the top as I am not a HUGE company but I do want it to be professional and easy to view and navigate.
Should not have
• Bright colors
• My logo is bright orange and black. I have also used dark grey and orange. See below:
• Orange:
• C = 0
• M = 64
• Y = 100
• K = 0
• Gray:
• C = 67
• M = 60
• Y = 59
• K = 45
• Font: Gotham Book and Gotham Bold

```html
<!DOCTYPE html>
<html lang="en">
<head>
<meta charset="utf-8">
<title>Alder Peak Events</title>
<link href="https://fonts.googleapis.com/css2?family=Open+Sans:wght@400;600;700&display=swap" rel="stylesheet">
<style>
:root{
  --teal:#3b8ba1;
  --teal-dark:#2b6b86;
  --navy:#215a74;
  --ink:#2b2b2b;
  --muted:#666;
  --card:#f5f5f5;
  --line:#e1e1e1;
  --footer:#f3f3f3;
  --white:#fff;
  --star:#f5a623;
}
*{margin:0;padding:0;box-sizing:border-box}
html,body{width:1200px;height:2356px;overflow:hidden}
body{font-family:"Open Sans",Arial,sans-serif;color:var(--ink);background:var(--white);position:relative}
.abs{position:absolute}

/* header */
.site-header{position:absolute;left:0;top:0;width:1200px;height:96px;border-top:3px solid var(--teal);background:var(--white)}
.brand{position:absolute;left:132px;top:26px;display:flex;align-items:center;gap:12px}
.brand-mark{width:34px;height:34px;background:var(--teal)}
.brand-name{font-size:22px;font-weight:600;color:var(--navy)}
.main-nav a{position:absolute;top:36px;font-size:13px;color:var(--ink);text-decoration:none}
.main-nav .active{left:446px;top:14px;width:60px;height:62px;border:3px solid var(--teal);padding:4px}
.main-nav .active span{display:flex;width:100%;height:100%;background:var(--navy);color:var(--white);align-items:center;justify-content:center;font-size:13px}
.login-btn{position:absolute;left:949px;top:28px;width:119px;height:36px;background:var(--teal);color:var(--white);font-size:14px;font-weight:600;display:flex;align-items:center;justify-content:center;border-radius:2px}

/* hero */
.hero{position:absolute;left:0;top:96px;width:1200px;height:502px;background:linear-gradient(135deg,#3d3a36 0%,#5c5750 40%,#2e3238 75%,#1e2228 100%)}
.hero-title{position:absolute;left:130px;top:160px;font-size:45px;font-weight:700;color:var(--white)}
.hero-text{position:absolute;left:132px;top:222px;width:420px;font-size:15.5px;line-height:25px;color:var(--white)}
.btn-solid{position:absolute;background:var(--teal);color:var(--white);font-size:13.5px;font-weight:600;display:flex;align-items:center;justify-content:center;border-radius:2px}
.hero-arrows{position:absolute;left:132px;top:426px;display:flex;gap:10px}
.hero-arrows span{width:24px;height:24px;border-radius:50%;background:#1b1b1b;display:flex;align-items:center;justify-content:center}

/* section titles */
.section-title{position:absolute;left:0;width:1200px;text-align:center;font-size:28px;font-weight:600;color:var(--ink)}
.section-lede{position:absolute;left:250px;width:700px;text-align:center;font-size:12.5px;line-height:20px;color:var(--muted)}

/* services */
.service-card{position:absolute;top:809px;width:295px;height:201px;background:var(--card);border:1px solid var(--line);text-align:center}
.service-card h3{position:absolute;left:0;top:79px;width:100%;font-size:13px;font-weight:700;color:var(--ink)}
.service-card p{position:absolute;left:30px;top:100px;width:235px;font-size:12px;line-height:20px;color:var(--muted)}
.service-card .more{position:absolute;left:139px;top:172px}
.diamond{position:absolute;top:746px;width:126px;height:126px}

/* about */
.about{position:absolute;left:0;top:1063px;width:1200px;height:430px}
.about h2{position:absolute;left:132px;top:58px;font-size:27px;font-weight:600;color:var(--white)}
.about p{position:absolute;left:132px;width:480px;font-size:12px;line-height:21px;color:var(--white)}
.btn-outline{position:absolute;left:132px;top:324px;width:121px;height:35px;border:1px solid var(--white);color:var(--white);font-size:13px;font-weight:600;display:flex;align-items:center;justify-content:center;border-radius:2px}
.screen-visual{position:absolute;left:748px;top:1118px;width:320px;height:324px;border-radius:6px;background:linear-gradient(180deg,#dfe4e8 0%,#b9c3ca 70%,#9aa4ab 100%)}

/* testimonials */
.testimonial{position:absolute;top:1602px;width:468px;height:134px;border-left:1px solid var(--line);border-right:1px solid var(--line)}
.avatar{position:absolute;left:36px;top:3px;width:102px;height:102px;border-radius:50%;background:linear-gradient(160deg,#c9c3bd,#8d8680)}
.quote{position:absolute;left:160px;top:22px;width:260px;font-size:11px;line-height:19px;font-style:italic;color:var(--muted)}
.qmark{position:absolute;font-size:26px;color:#aaa;font-family:Georgia,serif}
.author{position:absolute;left:176px;top:88px;font-size:11px;color:var(--muted)}
.author b{color:var(--navy)}
.stars{position:absolute;left:176px;top:112px;color:var(--star);font-size:11px;letter-spacing:1px}

/* specialties */
.specialties{position:absolute;left:0;top:1791px;width:1200px;height:282px;background:linear-gradient(180deg,#2a2623 0%,#1b1816 55%,#2c241c 100%)}
.specialties h2{position:absolute;left:0;top:48px;width:1200px;text-align:center;font-size:26px;font-weight:600;color:var(--white)}
.spec-item{position:absolute;top:116px;width:188px;text-align:center;color:var(--white);font-size:13.5px}
.spec-item .ring{width:66px;height:66px;margin:0 auto 22px;border:2px solid var(--white);border-radius:50%;display:flex;align-items:center;justify-content:center}
.spec-divider{position:absolute;top:112px;width:1px;height:116px;background:rgba(255,255,255,.75)}

/* footer */
.site-footer{position:absolute;left:0;top:2073px;width:1200px;height:283px;background:var(--footer)}
.footer-brand{position:absolute;left:132px;top:68px;display:flex;align-items:center;gap:12px}
.social{position:absolute;left:160px;top:128px;display:flex;gap:8px}
.social span{width:30px;height:30px;border:1px solid #777;border-radius:50%}
.footer-col h4{position:absolute;top:27px;font-size:15px;font-weight:400;color:var(--navy)}
.quick-links{position:absolute;left:432px;top:62px;list-style:none;font-size:11px;line-height:24px;color:var(--ink)}
.news-text{position:absolute;left:584px;top:58px;width:270px;font-size:11px;line-height:21px;color:var(--muted)}
.news-input{position:absolute;left:584px;top:109px;width:251px;height:36px;background:var(--white);border:1px solid var(--line);font-size:11px;color:var(--muted);padding:10px 14px}
.subscribe{position:absolute;left:584px;top:153px;width:82px;height:27px;background:var(--navy);color:var(--white);font-size:10px;font-weight:700;display:flex;align-items:center;justify-content:center;border-radius:2px}
.contact-list{position:absolute;left:905px;top:66px;list-style:none;font-size:11px;color:var(--ink)}
.contact-list li{display:flex;gap:12px;height:27px;align-items:flex-start}
.contact-list svg{flex:none;margin-top:2px}
.footer-rule{position:absolute;left:132px;top:230px;width:936px;height:1px;background:#ccc}
.copyright{position:absolute;left:0;top:246px;width:1200px;text-align:center;font-size:11px;color:var(--muted)}
</style>
</head>
<body>

<header class="site-header">
  <div class="brand"><span class="brand-mark"></span><span class="brand-name">Alder Peak Events</span></div>
  <nav class="main-nav">
    <a class="active" href="#"><span>Home</span></a>
    <a href="#" style="left:528px">About Us</a>
    <a href="#" style="left:614px">Services</a>
    <a href="#" style="left:694px">Testimonials</a>
    <a href="#" style="left:798px">Blog</a>
    <a href="#" style="left:858px">Contact Us</a>
  </nav>
  <div class="login-btn">Login / Register</div>
</header>

<section class="hero" role="img" aria-label="Overhead photo of a team planning an event around a table with laptops and floor plans">
  <h1 class="hero-title">Event Management</h1>
  <p class="hero-text">Lorem ipsum dolor sit amet, consectetur adipiscing ipsum elit, sed do eiusmod tempor incididunt...</p>
  <div class="btn-solid" style="left:132px;top:294px;width:118px;height:34px">Learn More Info</div>
  <div class="hero-arrows">
    <span><svg width="8" height="10"><path d="M6 1 2 5l4 4" stroke="#fff" stroke-width="1.6" fill="none"/></svg></span>
    <span><svg width="8" height="10"><path d="M2 1l4 4-4 4" stroke="#fff" stroke-width="1.6" fill="none"/></svg></span>
  </div>
</section>

<h2 class="section-title" style="top:638px">Our Services</h2>
<p class="section-lede" style="top:680px">Lorem ipsum dolor sit amet, consectetur adipiscing elit, sed do eiusmod tempor incididunt ut labore et dolore magna aliqua enim ad minim veniam, quis nostrud exercitation ullamco laboris</p>

<div class="service-card" style="left:132px"><h3>ALIQUIP EX EA COMMODO</h3><p>Lorem ipsum dolor sit amet, consectetur adipiscing elit, sed do eiusmod tempor incididunt labore dolore...</p><svg class="more" width="10" height="10"><path d="M2 2l6 6M8 3v5H3" stroke="#999" fill="none"/></svg></div>
<div class="service-card" style="left:452px"><h3>ALIQUIP EX EA COMMODO</h3><p>Lorem ipsum dolor sit amet, consectetur adipiscing elit, sed do eiusmod tempor incididunt labore dolore...</p><svg class="more" width="10" height="10"><path d="M2 2l6 6M8 3v5H3" stroke="#999" fill="none"/></svg></div>
<div class="service-card" style="left:773px"><h3>ALIQUIP EX EA COMMODO</h3><p>Lorem ipsum dolor sit amet, consectetur adipiscing elit, sed do eiusmod tempor incididunt labore dolore...</p><svg class="more" width="10" height="10"><path d="M2 2l6 6M8 3v5H3" stroke="#999" fill="none"/></svg></div>

<svg class="diamond" style="left:216px" viewBox="0 0 126 126"><path d="M63 2 124 63 63 124 2 63Z" fill="#fff" stroke="var(--teal)" stroke-width="3"/><path d="M63 11 115 63 63 115 11 63Z" fill="var(--navy)"/><g fill="#fff"><rect x="51" y="44" width="24" height="36"/></g><g fill="var(--navy)"><rect x="55" y="49" width="4" height="4"/><rect x="61" y="49" width="4" height="4"/><rect x="67" y="49" width="4" height="4"/><rect x="55" y="57" width="4" height="4"/><rect x="61" y="57" width="4" height="4"/><rect x="67" y="57" width="4" height="4"/><rect x="55" y="65" width="4" height="4"/><rect x="61" y="65" width="4" height="4"/><rect x="67" y="65" width="4" height="4"/><rect x="60" y="72" width="6" height="8"/></g></svg>
<svg class="diamond" style="left:537px" viewBox="0 0 126 126"><path d="M63 2 124 63 63 124 2 63Z" fill="#fff" stroke="var(--teal)" stroke-width="3"/><path d="M63 11 115 63 63 115 11 63Z" fill="var(--navy)"/><rect x="47" y="47" width="32" height="30" rx="2" fill="#fff"/><rect x="53" y="42" width="3" height="8" fill="#fff"/><rect x="70" y="42" width="3" height="8" fill="#fff"/><g fill="var(--navy)"><rect x="50" y="55" width="26" height="1.5"/><rect x="51" y="59" width="5" height="4"/><rect x="58" y="59" width="5" height="4"/><rect x="65" y="59" width="5" height="4"/><rect x="51" y="66" width="5" height="4"/><rect x="58" y="66" width="5" height="4"/><rect x="65" y="66" width="5" height="4"/></g></svg>
<svg class="diamond" style="left:857px" viewBox="0 0 126 126"><path d="M63 2 124 63 63 124 2 63Z" fill="#fff" stroke="var(--teal)" stroke-width="3"/><path d="M63 11 115 63 63 115 11 63Z" fill="var(--navy)"/><g fill="#fff"><circle cx="63" cy="52" r="6"/><path d="M52 74c0-9 5-14 11-14s11 5 11 14Z"/><circle cx="49" cy="56" r="4.5"/><path d="M40 74c0-7 4-11 9-11 2 0 3 .5 4 1-2 3-3 6-3 10Z"/><circle cx="77" cy="56" r="4.5"/><path d="M86 74c0-7-4-11-9-11-2 0-3 .5-4 1 2 3 3 6 3 10Z"/></g></svg>

<section class="about">
  <svg class="abs" width="1200" height="430" style="left:0;top:0"><rect width="1200" height="430" fill="var(--teal-dark)"/><path d="M0 0H801L613 214 801 430H0Z" fill="var(--teal)"/><path d="M801 0 613 214 801 430" stroke="#fff" stroke-width="3" fill="none"/></svg>
  <h2>About Us</h2>
  <p style="top:107px">Do you ever wish that you could shift the event planning responsibilities for your company toanother person who excels in the management of all details associated with putting on a great meeting or event? Well, you can... Alder Peak Events specializes in event management for associations, corporations, not for profit...</p>
  <p style="top:210px">After a successful 20+ year career coordinating events in the resort community of Vail Dana is now providing her skills on the other side of the table. When you hire Alder Peak Events you are hiring a company who is intimately familiar with the inner-workings of hotels, resorts and off-site hospitality venues...</p>
  <div class="btn-outline">Learn More Info</div>
</section>
<div class="screen-visual" role="img" aria-label="Desktop monitor showing a photo of a business meeting in a bright lounge"></div>

<h2 class="section-title" style="top:1540px">Testimonials</h2>
<div class="testimonial" style="left:132px">
  <div class="avatar" role="img" aria-label="Portrait photo of a client"></div>
  <span class="qmark" style="left:158px;top:-4px">&ldquo;</span>
  <p class="quote" style="left:178px">Lorem Ipsum is simply dummy text of the printing and typesetting industry. Lorem Ipsum has been the industry's standard dummy...</p>
  <span class="qmark" style="left:424px;top:58px">&rdquo;</span>
  <div class="author" style="left:176px;top:88px"><b>JOHN DOE</b> - Labore Dolore</div>
  <div class="stars">★★★★★</div>
</div>
<div class="testimonial" style="left:600px">
  <div class="avatar" role="img" aria-label="Portrait photo of a client" style="left:34px"></div>
  <span class="qmark" style="left:158px;top:-4px">&ldquo;</span>
  <p class="quote" style="left:178px">Lorem Ipsum is simply dummy text of the printing and typesetting industry. Lorem Ipsum has been the industry's standard dummy...</p>
  <span class="qmark" style="left:424px;top:58px">&rdquo;</span>
  <div class="author"><b>JOHN DOE</b> - Labore Dolore</div>
  <div class="stars">★★★★★</div>
</div>

<section class="specialties" role="img" aria-label="Dim photo of a boardroom with a long conference table">
  <h2>Specialties</h2>
  <svg class="abs" style="left:84px;top:140px" width="14" height="50"><path d="M12 2 2 25l10 23" stroke="#ccc" stroke-width="1.5" fill="none"/></svg>
  <svg class="abs" style="left:1100px;top:140px" width="14" height="50"><path d="M2 2l10 23-10 23" stroke="#ccc" stroke-width="1.5" fill="none"/></svg>
  <div class="spec-item" style="left:124px"><div class="ring"><svg width="22" height="30" viewBox="0 0 22 30"><path d="M11 1C5 1 1 5.5 1 11c0 7 10 18 10 18s10-11 10-18C21 5.5 17 1 11 1Z" fill="#fff"/><circle cx="11" cy="11" r="4" fill="#1b1816"/></svg></div>Venue Selection</div>
  <div class="spec-divider" style="left:320px"></div>
  <div class="spec-item" style="left:318px"><div class="ring"><svg width="28" height="30" viewBox="0 0 28 30"><path d="M3 5h22L14 17Z" fill="#fff"/><path d="M14 17v10M8 28h12" stroke="#fff" stroke-width="2"/><circle cx="22" cy="5" r="4" fill="none" stroke="#fff" stroke-width="1.6"/></svg></div>Food and Beverage</div>
  <div class="spec-divider" style="left:506px"></div>
  <div class="spec-item" style="left:506px"><div class="ring"><svg width="30" height="30" viewBox="0 0 30 30"><circle cx="15" cy="13" r="7" fill="#fff"/><rect x="12" y="20" width="6" height="6" fill="#fff"/><g stroke="#fff" stroke-width="1.6"><path d="M15 1v3M4 4l2 2M26 4l-2 2M1 13h3M26 13h3"/></g></svg></div>Program Planning</div>
  <div class="spec-divider" style="left:694px"></div>
  <div class="spec-item" style="left:693px"><div class="ring"><svg width="30" height="28" viewBox="0 0 30 28"><path d="M2 10h6l8-7v22l-8-7H2Z" fill="#fff"/><path d="M20 9c2 3 2 7 0 10M23 6c4 5 4 11 0 16" stroke="#fff" stroke-width="1.8" fill="none"/></svg></div>Audio Visual Expertise</div>
  <div class="spec-divider" style="left:881px"></div>
  <div class="spec-item" style="left:881px"><div class="ring"><svg width="22" height="30" viewBox="0 0 22 30"><rect x="2" y="1" width="18" height="28" fill="none" stroke="#fff" stroke-width="2"/><g fill="#fff"><rect x="6" y="5" width="3" height="3"/><rect x="13" y="5" width="3" height="3"/><rect x="6" y="11" width="3" height="3"/><rect x="13" y="11" width="3" height="3"/><rect x="6" y="17" width="3" height="3"/><rect x="13" y="17" width="3" height="3"/><rect x="9" y="23" width="4" height="6"/></g></svg></div>Room Block Management</div>
</section>

<footer class="site-footer">
  <div class="footer-brand"><span class="brand-mark"></span><span class="brand-name">Alder Peak Events</span></div>
  <div class="social"><span></span><span></span><span></span><span></span><span></span></div>

  <div class="footer-col"><h4 style="left:432px">Quick Links</h4></div>
  <ul class="quick-links"><li>Home</li><li>About Us</li><li>Services</li><li>Testimonials</li><li>Blog</li><li>Contact us</li></ul>

  <div class="footer-col"><h4 style="left:583px">Newsletter</h4></div>
  <p class="news-text">Enter your email address to receive the latest news and notes from our blog.</p>
  <div class="news-input">Enter Your Mail Id</div>
  <div class="subscribe">SUBSCRIBE</div>

  <div class="footer-col"><h4 style="left:905px">Contact us</h4></div>
  <ul class="contact-list">
    <li><svg width="12" height="11" viewBox="0 0 12 11"><path d="M1 4c0-2 2-3 5-3s5 1 5 3H8V3H4v1ZM2 5h8v5H2Z" fill="#444"/></svg>(555) 214-0187</li>
    <li><svg width="12" height="11" viewBox="0 0 12 11"><rect x="3" y="0" width="6" height="3" fill="#444"/><rect x="0" y="3" width="12" height="5" fill="#444"/><rect x="3" y="7" width="6" height="4" fill="#444"/></svg>(555) 214-0187</li>
    <li><svg width="12" height="9" viewBox="0 0 12 9"><rect x="0" y="0" width="12" height="9" fill="#444"/><path d="M0 0l6 5 6-5" stroke="#fff" fill="none"/></svg><span style="text-decoration:underline">hello@alderpeakevents.com</span></li>
    <li><svg width="12" height="14" viewBox="0 0 12 14"><path d="M6 0C3 0 1 2 1 5c0 4 5 9 5 9s5-5 5-9c0-3-2-5-5-5Z" fill="#444"/><circle cx="6" cy="5" r="2" fill="#fff"/></svg><span style="width:150px;line-height:16px">#2868 Lorem ipsum dolor sit amet, consectetur</span></li>
  </ul>

  <div class="footer-rule"></div>
  <p class="copyright">Copyrights ©2017 Alder Peak Events | All rights reserved.</p>
</footer>

</body>
</html>
```